Business Card Design

Hi I need a business card designed, we already have the business name logo artwork and would like some concept ideas for the Bus Card layout.
On the back of the card i want to include the products and services that we offer.
We are a Plastics Sheeting manufacture based in Perth Australia.

                                       

We need a BC design for a company called Tarnby Plastics based in Perth Australia.

We supply from DIY to Trade & Industrial  Engineering Markets.

We specialise in:

·         Cut to size panels  (all shapes and sizes)

·         Plastics fabrication & Welding

·         Custom Designs

·         Plastic Repairs

·         PVC Pipe Slotting & PVC Pipe Threading

·         Supplier of all types of engineering plastics and profiles.

Including:           Acrylic / Vendrix

                               Polycarbonate / Moravite

                               Prismatic Light Diffuser

                               Tubrasin

                               HDPE / UHMWPE

                               PVC / PVC Foam

                               Nylon

                               HIPS

```html
<!DOCTYPE html>
<html lang="en">
<head>
<meta charset="utf-8">
<title>Tarnby Plastics – Business Card</title>
<link rel="stylesheet" href="https://fonts.googleapis.com/css2?family=Barlow:ital,wght@0,400;0,700;1,400&display=swap">
<style>
  :root {
    --page-bg: #e4e2df;
    --frost-top: #f3f1ee;
    --frost-bottom: #dcd8d3;
    --navy: #0b2a5e;
    --ink: #1d2a44;
    --muted: #6f6f72;
    --white: #ffffff;
    --dot-red: #c8202f;
    --dot-orange: #e0782a;
    --dot-yellow: #e3b21f;
    --dot-blue: #2a8fd0;
    --dot-green: #3f9a3a;
  }
  * { box-sizing: border-box; margin: 0; padding: 0; }
  html, body {
    width: 1200px;
    height: 970px;
    overflow: hidden;
    background: var(--page-bg);
    font-family: "Barlow", Arial, sans-serif;
  }
  .business-card {
    position: absolute;
    left: 60px;
    top: 185px;
    width: 1080px;
    height: 600px;
    overflow: hidden;
    box-shadow: 0 12px 30px rgba(0,0,0,0.18);
  }
  .card-identity {
    position: absolute;
    inset: 0 0 auto 0;
    height: 346px;
    background: linear-gradient(180deg, var(--frost-top), var(--frost-bottom));
  }
  .brand-name {
    position: absolute;
    right: 59px;
    top: 36px;
    font-weight: 700;
    font-size: 78px;
    line-height: 1;
    color: var(--ink);
    white-space: nowrap;
  }
  .cardholder {
    position: absolute;
    right: 78px;
    top: 222px;
    text-align: right;
  }
  .cardholder-name {
    font-weight: 700;
    font-size: 33px;
    letter-spacing: 1px;
    text-transform: uppercase;
    color: var(--ink);
    line-height: 1.1;
  }
  .cardholder-role {
    font-weight: 400;
    font-size: 27px;
    color: var(--muted);
    line-height: 1.3;
  }
  .services-band {
    position: absolute;
    left: 0;
    right: 0;
    bottom: 0;
    height: 254px;
    background: var(--navy);
    padding: 24px 0 0 155px;
  }
  .service-list { list-style: none; }
  .service-item {
    font-style: italic;
    font-size: 33px;
    line-height: 38.6px;
    color: var(--white);
    white-space: nowrap;
  }
  .dot {
    display: inline-block;
    width: 11px;
    height: 11px;
    border-radius: 50%;
    margin: 0 12px 5px 0;
    vertical-align: middle;
  }
  .dot + .dot, .service-item .spacer { margin-left: 0; }
  .inline-gap { display: inline-block; width: 10px; }
  .dot-red { background: var(--dot-red); }
  .dot-orange { background: var(--dot-orange); }
  .dot-yellow { background: var(--dot-yellow); }
  .dot-blue { background: var(--dot-blue); }
  .dot-green { background: var(--dot-green); }
</style>
</head>
<body>
  <article class="business-card">
    <section class="card-identity">
      <div class="brand-name">Tarnby Plastics</div>
      <div class="cardholder">
        <div class="cardholder-name">Cardholder Name</div>
        <div class="cardholder-role">Designation</div>
      </div>
    </section>
    <section class="services-band">
      <ul class="service-list">
        <li class="service-item"><span class="dot dot-red"></span>Cut to size panels (all shapes and sizes)</li>
        <li class="service-item"><span class="dot dot-orange"></span>Plastics fabrication &amp; Welding</li>
        <li class="service-item"><span class="dot dot-yellow"></span>Custom Designs<span class="inline-gap"></span><span class="dot dot-blue"></span>Plastic Repairs</li>
        <li class="service-item"><span class="dot dot-green"></span>PVC Pipe Slotting &amp; PVC Pipe Threading</li>
        <li class="service-item"><span class="dot dot-red"></span>All types of engineering plastics &amp; profiles</li>
      </ul>
    </section>
  </article>
</body>
</html>
```